Business card for a shipping supplies business

Needing a business card design. Please see the logo. The logo with the white font should be used if there is a dark background.

We are looking for the following info on the card. Please see the sample info. We will need the info to be changed with a few different employee names and info but all will use the same template.

Business Name: The Crate Heron
Employee Name : Derek Malloy
Position: Account Manager
Address: 4827 W. Ridge 918 S.
Fort Worth, TX 72348
email: Derek@thecrateheron.com
telephone: 866-417-2902 x 217
website: www.getcartonry.com

Target Market(s)

Businesses who ship products for online sales

Industry/Entity Type

Cardboard

Contact Information for Business Card

Name, title, address, website, logo, telephone number

Font styles to use
Sans Serif

Colors
EE7325
F08F49
F5BC92
FAE3D3
FDF4ED

Requirements
Must have
• Logo on back of card. Clean look, just logo, website address

```html
<!DOCTYPE html>
<html lang="en">
<head>
<meta charset="utf-8">
<title>The Crate Heron – Business Card</title>
<link rel="stylesheet" href="https://fonts.googleapis.com/css2?family=Montserrat:wght@700;800&family=Open+Sans:wght@400;600;700&display=swap">
<style>
  :root {
    --canvas: #e3e3e3;
    --card-dark: #752516;
    --accent: #c9552a;
    --accent-deep: #5a1a0e;
    --panel: #f4f4f4;
    --ink: #1f1f1f;
    --white: #ffffff;
  }
  * { margin: 0; padding: 0; box-sizing: border-box; }
  html, body { width: 1200px; height: 960px; overflow: hidden; }
  body {
    background: var(--canvas);
    position: relative;
    font-family: "Open Sans", Arial, sans-serif;
  }
  .card {
    position: absolute;
    left: 308px;
    width: 583px;
    height: 332px;
    background: var(--card-dark);
    overflow: hidden;
  }
  .card-front { top: 125px; }
  .card-back { top: 510px; }

  .front-brand {
    position: absolute;
    left: 0; right: 0;
    top: 0; bottom: 0;
    display: flex;
    align-items: center;
    justify-content: center;
    flex-direction: column;
    gap: 18px;
  }
  .brand-mark {
    width: 22px; height: 22px;
    border-radius: 50%;
    background: var(--accent);
  }
  .brand-name {
    font-family: "Montserrat", Arial, sans-serif;
    font-weight: 800;
    color: var(--white);
    letter-spacing: 1px;
    text-transform: uppercase;
  }
  .front-brand .brand-name { font-size: 38px; }

  .back-brand {
    position: absolute;
    left: 40px;
    top: 100px;
    width: 190px;
    height: 150px;
    display: flex;
    flex-direction: column;
    align-items: center;
    justify-content: center;
    gap: 12px;
    text-align: center;
  }
  .back-brand .brand-name { font-size: 24px; line-height: 1.2; }

  .back-shapes { position: absolute; inset: 0; }

  .contact-block {
    position: absolute;
    right: 57px;
    text-align: right;
    color: var(--ink);
    font-size: 14px;
    line-height: 20px;
  }
  .person { top: 95px; }
  .person-name {
    color: var(--accent);
    font-weight: 700;
    font-size: 18px;
    line-height: 22px;
    text-transform: uppercase;
  }
  .address { top: 146px; }
  .reach { top: 193px; }
  .website { color: var(--accent); font-weight: 700; }
</style>
</head>
<body>

  <section class="card card-front" aria-label="Card front">
    <div class="front-brand">
      <span class="brand-mark"></span>
      <span class="brand-name">The Crate Heron</span>
    </div>
  </section>

  <section class="card card-back" aria-label="Card back">
    <svg class="back-shapes" width="583" height="332" viewBox="0 0 583 332">
      <!-- white info panel and accent edge -->
      <polygon points="379,0 389,0 255,332 245,332" fill="var(--accent)"/>
      <polygon points="389,0 583,0 583,332 255,332" fill="var(--panel)"/>
      <!-- icon tab -->
      <polygon points="297,90 352,90 283,262 245,262" fill="var(--accent)"/>
      <polygon points="245,262 283,262 275,286" fill="var(--accent-deep)"/>
      <!-- divider rules -->
      <line x1="333" y1="144" x2="583" y2="144" stroke="var(--accent)" stroke-width="1.5"/>
      <line x1="314" y1="190" x2="583" y2="190" stroke="var(--accent)" stroke-width="1.5"/>
      <line x1="292" y1="144" x2="333" y2="144" stroke="var(--card-dark)" stroke-width="1.5"/>
      <line x1="273" y1="190" x2="314" y2="190" stroke="var(--card-dark)" stroke-width="1.5"/>
      <!-- person icon -->
      <g fill="var(--white)">
        <circle cx="320" cy="111" r="4"/>
        <path d="M313 123 q0 -7 7 -7 q7 0 7 7 z"/>
      </g>
      <!-- pin icon -->
      <path d="M300 158 a5 5 0 0 1 5 5 c0 4 -5 10 -5 10 c0 0 -5 -6 -5 -10 a5 5 0 0 1 5 -5 z" fill="var(--white)"/>
      <circle cx="300" cy="163" r="1.8" fill="var(--accent)"/>
      <!-- phone icon -->
      <path d="M281 200 l3 -1 l2 4 l-2 1.5 q1.5 3 4 4 l1.5 -2 l4 2 l-1 3 q-8 0 -11.5 -11.5 z" fill="var(--white)"/>
      <!-- mail icon -->
      <g>
        <rect x="270" y="222" width="13" height="9" fill="var(--white)"/>
        <path d="M270 222 l6.5 5 l6.5 -5" fill="none" stroke="var(--accent)" stroke-width="1.2"/>
      </g>
      <!-- globe icon -->
      <g fill="none" stroke="var(--white)" stroke-width="1.2">
        <circle cx="268" cy="246" r="5.5"/>
        <ellipse cx="268" cy="246" rx="2.3" ry="5.5"/>
        <line x1="262.5" y1="246" x2="273.5" y2="246"/>
      </g>
    </svg>

    <div class="back-brand">
      <span class="brand-mark"></span>
      <span class="brand-name">The Crate Heron</span>
    </div>

    <div class="contact-block person">
      <p class="person-name">Derek Malloy</p>
      <p class="person-title">Account Manager</p>
    </div>
    <div class="contact-block address">
      <p>4827 W. Ridge 918 S.</p>
      <p>Fort Worth, TX 72348</p>
    </div>
    <div class="contact-block reach">
      <p>866-417-2902 x 217</p>
      <p>Derek@thecrateheron.com</p>
      <p class="website">www.getcartonry.com</p>
    </div>
  </section>

</body>
</html>
```